Bref créative
VORTELL STATIONERY
STATIONERY PROJECT
I need double sided standard sized Business Card [3.5" x 2"]
The logo's font has to be the same. The other font doesnt have to be ***FOR NOW***
Bright & Fun-filled
Tomas R. Weller
Sales
PO BOX 482730
Miami, FL 33158
Sales@Vortell-example.com
www.Vortell-example.com
make this like a list of products we offer:
CHEMICALS-
NAPKINS-
UTENSILS-
MOPS/BROOMS-
TOILET PAPER-
CFOLD TOWELS-
DISPENSERS-
ANTIBACTERIAL PRODUCTS-
TRASH CAN LINERS-
FOAM CUPS-

```html
<!DOCTYPE html>
<html lang="en">
<head>
<meta charset="utf-8">
<title>Vortell Business Card</title>
<link rel="stylesheet" href="https://fonts.googleapis.com/css2?family=Arimo:wght@400;700&display=swap">
<style>
  :root {
    --backdrop: #2b2b2b;
    --card: #ffffff;
    --brand-blue: #0f5f93;
    --brand-blue-dark: #0a4a75;
    --brand-green: #4e9a3a;
    --brand-green-light: #8cc63f;
    --ink: #4a4a4a;
    --rule: #c9c9c9;
  }
  * { margin: 0; padding: 0; box-sizing: border-box; }
  html, body {
    width: 1200px;
    height: 780px;
    overflow: hidden;
    background: var(--backdrop);
    font-family: "Arimo", Arial, sans-serif;
  }
  .business-card {
    position: absolute;
    left: 100px;
    top: 104px;
    width: 1000px;
    height: 572px;
    background: var(--card);
    border-radius: 40px;
    overflow: hidden;
  }
  .brand-lockup {
    position: absolute;
    left: 80px;
    top: 70px;
    display: flex;
    align-items: center;
    gap: 34px;
  }
  .brand-dot {
    width: 150px;
    height: 150px;
    border-radius: 50%;
    background: var(--brand-blue);
  }
  .brand-name {
    font-weight: 700;
    font-size: 128px;
    letter-spacing: 2px;
    line-height: 1;
    color: var(--brand-blue);
  }
  .person {
    position: absolute;
    right: 558px;
    top: 316px;
    text-align: right;
  }
  .person-name {
    font-weight: 700;
    font-size: 32px;
    color: var(--brand-blue);
  }
  .person-role {
    font-weight: 700;
    font-size: 24px;
    color: var(--brand-green);
    margin-top: 6px;
  }
  .divider {
    position: absolute;
    left: 462px;
    top: 262px;
    width: 2px;
    height: 162px;
    background: var(--rule);
  }
  .contact {
    position: absolute;
    left: 490px;
    top: 262px;
    color: var(--ink);
    font-size: 24px;
    line-height: 1.35;
  }
  .contact-line {
    display: flex;
    align-items: center;
    gap: 14px;
  }
  .contact-address { margin-bottom: 10px; }
  .contact-icon {
    width: 24px;
    height: 28px;
    flex: none;
  }
  .contact-at {
    width: 24px;
    text-align: center;
    font-weight: 700;
    color: var(--brand-blue);
  }
  .footer-band {
    position: absolute;
    left: 0;
    bottom: 0;
    width: 1000px;
    height: 150px;
  }
  .website {
    position: absolute;
    left: 0;
    right: 0;
    bottom: 36px;
    text-align: center;
    color: #ffffff;
    font-size: 26px;
  }
</style>
</head>
<body>
  <main class="business-card">
    <div class="brand-lockup">
      <div class="brand-dot"></div>
      <div class="brand-name">VORTELL</div>
    </div>

    <div class="person">
      <div class="person-name">Tomas R. Weller</div>
      <div class="person-role">Sales</div>
    </div>

    <div class="divider"></div>

    <div class="contact">
      <div class="contact-address">PO BOX 482730 Miami,<br>FL 33158</div>
      <div class="contact-line">
        <svg class="contact-icon" viewBox="0 0 24 28" aria-hidden="true">
          <rect x="5" y="1" width="14" height="26" rx="3" fill="none" stroke="#0f5f93" stroke-width="2.5"/>
          <rect x="8" y="5" width="8" height="12" fill="#0f5f93"/>
          <circle cx="12" cy="22" r="1.8" fill="#0f5f93"/>
        </svg>
        <span>3055550147</span>
      </div>
      <div class="contact-line">
        <span class="contact-at">@</span>
        <span>Sales@Vortell-example.com</span>
      </div>
    </div>

    <svg class="footer-band" viewBox="0 0 1000 150" preserveAspectRatio="none" aria-hidden="true">
      <defs>
        <linearGradient id="bandBlue" x1="0" y1="0" x2="0" y2="1">
          <stop offset="0" stop-color="#1677b3"/>
          <stop offset="1" stop-color="#0a4a75"/>
        </linearGradient>
        <linearGradient id="bandGreen" x1="0" y1="0" x2="1" y2="0">
          <stop offset="0" stop-color="#8cc63f"/>
          <stop offset="1" stop-color="#3f8a32"/>
        </linearGradient>
      </defs>
      <path d="M0 18 C 300 40, 650 80, 1000 62 L1000 150 L0 150 Z" fill="url(#bandGreen)"/>
      <path d="M0 34 C 300 56, 650 92, 1000 74 L1000 150 L0 150 Z" fill="#ffffff"/>
      <path d="M0 42 C 300 64, 650 98, 1000 82 L1000 150 L0 150 Z" fill="url(#bandBlue)"/>
    </svg>
    <div class="website">www.Vortell-example.com</div>
  </main>
</body>
</html>
```